HomeBridle business card and stationary design

We are looking for a simple yet elegant design for our mortgage company business card and stationary.

The card should include:
Name (Derek Walsh)
Title (CEO)
Phone Number (614-208-3917)
Address (48 Birchfield Court, Suite 314, Marlow, OH 43952)
Email (email@homebridle-example.com)
"NMLS" i.e. (NMLS 61947)
"Company NMLS" (Company NMLS 472815)

See above

```html
<!DOCTYPE html>
<html lang="en">
<head>
<meta charset="UTF-8">
<title>HomeBridle Business Card</title>
<link href="https://fonts.googleapis.com/css2?family=Montserrat:wght@400;500;800&display=swap" rel="stylesheet">
<style>
  :root {
    --navy: #111c26;
    --navy-light: #1b2833;
    --blue: #06a6e6;
    --white: #ffffff;
    --paper: #f1f2f3;
    --paper-shade: #e3e5e7;
    --ink: #2a2f35;
    --page: #ffffff;
  }
  * { box-sizing: border-box; margin: 0; padding: 0; }
  html, body {
    width: 734px; height: 1200px; overflow: hidden;
    background: var(--page);
    font-family: "Montserrat", sans-serif;
  }
  .sheet {
    width: 734px; height: 1200px;
    display: flex; flex-direction: column; align-items: center; justify-content: center;
    gap: 46px;
  }
  .card {
    position: relative;
    width: 620px; height: 354px;
    overflow: hidden;
    box-shadow: 0 6px 12px rgba(0,0,0,0.28);
  }
  .card-front {
    background: linear-gradient(135deg, var(--navy) 0%, var(--navy-light) 45%, var(--navy) 55%, var(--navy-light) 80%, var(--navy) 100%);
  }
  .brand-name {
    position: absolute; left: 0; right: 0; top: 140px;
    text-align: center;
    font-weight: 500; font-size: 56px; letter-spacing: 0.5px;
    color: var(--white);
  }
  .front-rule {
    position: absolute; left: 0; right: 0; top: 323px; height: 1px;
    background: linear-gradient(90deg, transparent, rgba(255,255,255,0.8) 25%, rgba(255,255,255,0.8) 75%, transparent);
  }
  .url-tab {
    position: absolute; left: 198px; top: 314px; width: 224px; height: 19px;
    background: var(--blue);
    clip-path: polygon(6% 0, 94% 0, 100% 100%, 0 100%);
    color: var(--white); font-size: 13px; letter-spacing: 1.6px;
    text-align: center; line-height: 19px;
  }
  .card-back {
    background: linear-gradient(135deg, var(--paper) 0%, var(--white) 40%, var(--paper-shade) 70%, var(--white) 100%);
  }
  .back-art { position: absolute; inset: 0; }
  .back-brand {
    position: absolute; left: 20px; top: 160px; width: 210px;
    text-align: center;
    font-weight: 500; font-size: 30px; color: var(--white);
  }
  .contact {
    position: absolute; left: 324px; top: 96px;
    color: var(--ink);
  }
  .contact-name {
    font-weight: 800; font-size: 21px; color: var(--blue); letter-spacing: 0.3px; line-height: 1.1;
  }
  .contact-title { font-size: 14px; margin-bottom: 12px; }
  .contact-list { list-style: none; }
  .contact-list li {
    display: flex; align-items: center; gap: 8px;
    font-size: 12px; height: 25px;
  }
  .contact-list svg { width: 11px; height: 11px; fill: var(--blue); flex: none; }
  .licence { font-size: 9px; margin-top: 6px; }
</style>
</head>
<body>
<main class="sheet">
  <section class="card card-front">
    <div class="brand-name">HomeBridle</div>
    <div class="front-rule"></div>
    <div class="url-tab">www.homebridle.com</div>
  </section>

  <section class="card card-back">
    <svg class="back-art" viewBox="0 0 620 354" width="620" height="354">
      <polygon points="0,0 232,0 280,177 232,354 0,354" fill="#111c26"/>
      <polyline points="251,47 295,177 254,306" fill="none" stroke="#06a6e6" stroke-width="9"/>
    </svg>
    <div class="back-brand">HomeBridle</div>
    <div class="contact">
      <div class="contact-name">DEREK WALSH</div>
      <div class="contact-title">CEO</div>
      <ul class="contact-list">
        <li><svg viewBox="0 0 24 24"><path d="M6.6 10.8a15 15 0 0 0 6.6 6.6l2.2-2.2a1 1 0 0 1 1-.25 11 11 0 0 0 3.6.6 1 1 0 0 1 1 1V20a1 1 0 0 1-1 1A17 17 0 0 1 3 4a1 1 0 0 1 1-1h3.5a1 1 0 0 1 1 1c0 1.25.2 2.45.6 3.6a1 1 0 0 1-.25 1z"/></svg>614-208-3917</li>
        <li><svg viewBox="0 0 24 24"><path d="M2 5h20v14H2z M2 5l10 8 10-8" /></svg>email@homebridle-example.com</li>
        <li><svg viewBox="0 0 24 24"><circle cx="12" cy="12" r="10"/></svg>www.homebridle.com</li>
        <li><svg viewBox="0 0 24 24"><path d="M12 2a7 7 0 0 0-7 7c0 5 7 13 7 13s7-8 7-13a7 7 0 0 0-7-7zm0 9.5A2.5 2.5 0 1 1 12 6.5a2.5 2.5 0 0 1 0 5z"/></svg>48 Birchfield Court, Suite 314, Marlow, OH 43952</li>
      </ul>
      <div class="licence">"NMLS" i.e. (NMLS 61947) | Company NMLS 472815</div>
    </div>
  </section>
</main>
</body>
</html>
```